Yoga for Scoliosis business card/logo design

I need a business card/logo design for my new business. I am a registered yoga teacher and am certified in yoga for scoliosis. I'd like my card to read "Marlow Yoga Yoga for a Healthy Spine" and would like to incorporate one of the letters in my name{ ie the first vertical line of the letter " H "or "D"} to resemble a scoliotic spine. I regularly teach the following:Yoga for Scoliosis, Yoga for Back Health, Hatha yoga, Vinyasa yoga with Iyengar style alignment. This business is mostly for private clients, but I also teach group, semi-private & work shop classes. I like the colors green (light emerald) and royal blue. I'd like the design to be somewhat sleek, but not too modern. I also like the idea of a ying/yang symbol with a scoliotic spine dviding it.

Industry/Entity Type

Teacher

Contact Information for Business Card

Tamsin Marlow
200 RYT, Certified Yoga for Scoliosis Instructor
MarlowYoga.example
MarlowYoga@mailbox.example
415-629-3174

```html
<!DOCTYPE html>
<html lang="en">
<head>
<meta charset="utf-8">
<title>Marlow Yoga – Business Card</title>
<link rel="stylesheet" href="https://fonts.googleapis.com/css2?family=Libre+Baskerville:wght@700&family=Arimo:wght@400&display=swap">
<style>
  :root {
    --page-bg: #e9ecea;
    --card-bg: #ffffff;
    --royal-blue: #2a4fa8;
    --emerald: #3fbf8a;
    --ink: #1a1a1a;
    --photo-light: #d9b49a;
    --photo-mid: #a97858;
    --photo-dark: #5e3a24;
    --glow: #f2a93a;
  }
  * { margin: 0; padding: 0; box-sizing: border-box; }
  html, body {
    width: 1200px; height: 800px; overflow: hidden;
    background: var(--page-bg);
  }
  .card {
    position: absolute; left: 100px; top: 115px;
    width: 1000px; height: 571px;
    background: var(--card-bg);
    overflow: hidden;
    box-shadow: 0 10px 30px rgba(0,0,0,.18);
  }
  .card-art { position: absolute; inset: 0; }
  .card-text { position: absolute; left: 70px; top: 58px; }
  .brand-name {
    font-family: "Libre Baskerville", Georgia, serif;
    font-weight: 700; font-size: 58px; line-height: 1;
    color: var(--royal-blue); letter-spacing: 1px;
  }
  .tagline {
    font-family: "Arimo", Arial, sans-serif;
    font-size: 20px; color: var(--ink); margin: 8px 0 0 4px;
  }
  .owner-name {
    font-family: "Libre Baskerville", Georgia, serif;
    font-weight: 700; font-size: 30px; color: var(--royal-blue);
    margin-top: 44px;
  }
  .credential {
    font-family: "Arimo", Arial, sans-serif;
    font-size: 22px; color: var(--ink); margin-top: 26px;
  }
  .contact-list { list-style: none; margin-top: 40px; }
  .contact-item {
    display: flex; align-items: center; gap: 12px;
    font-family: "Arimo", Arial, sans-serif;
    font-size: 21px; color: var(--ink); line-height: 1.45;
  }
  .contact-icon { width: 18px; height: 18px; fill: var(--emerald); flex: none; }
</style>
</head>
<body>
  <div class="card">
    <svg class="card-art" viewBox="0 0 1000 571" preserveAspectRatio="none">
      <defs>
        <linearGradient id="photoTone" x1="0" y1="0" x2="1" y2="1">
          <stop offset="0" stop-color="var(--photo-light)"/>
          <stop offset=".55" stop-color="var(--photo-mid)"/>
          <stop offset="1" stop-color="var(--photo-dark)"/>
        </linearGradient>
        <radialGradient id="candleGlow" cx="800" cy="440" r="170" gradientUnits="userSpaceOnUse">
          <stop offset="0" stop-color="var(--glow)" stop-opacity=".6"/>
          <stop offset="1" stop-color="var(--glow)" stop-opacity="0"/>
        </radialGradient>
      </defs>
      <g role="img" aria-label="Photograph of stacked spa stones with bamboo leaves and lit candles">
        <path d="M575 0 L1000 0 L1000 540 C860 500 770 390 715 330 C660 250 625 150 575 0 Z" fill="url(#photoTone)"/>
        <path d="M575 0 L1000 0 L1000 540 C860 500 770 390 715 330 C660 250 625 150 575 0 Z" fill="url(#candleGlow)"/>
      </g>
      <path class="spine-band" d="M575 -4 C625 150 660 250 715 330 S860 500 1004 542" fill="none" stroke="var(--royal-blue)" stroke-width="16"/>
      <path class="spine-accent" d="M560 -4 C610 150 645 252 700 334 S846 506 1004 558" fill="none" stroke="var(--emerald)" stroke-width="5"/>
    </svg>

    <div class="card-text">
      <h1 class="brand-name">Marlow Yoga</h1>
      <p class="tagline">Yoga for a Healthy Spine</p>
      <h2 class="owner-name">Tamsin Marlow</h2>
      <p class="credential">200 RYT, Certified Yoga for Scoliosis Instructor</p>
      <ul class="contact-list">
        <li class="contact-item">
          <svg class="contact-icon" viewBox="0 0 24 24"><path d="M3 8c0-3 4-5 9-5s9 2 9 5v2h-5V8c-1-1-7-1-8 0v2H3zM6 12h12l3 9H3z"/></svg>
          415-629-3174
        </li>
        <li class="contact-item">
          <svg class="contact-icon" viewBox="0 0 24 24"><circle cx="12" cy="12" r="10"/><path d="M8 6c3 1 2 4 5 4s1 4 4 5" stroke="#fff" stroke-width="2" fill="none"/></svg>
          MarlowYoga.example
        </li>
        <li class="contact-item">
          <svg class="contact-icon" viewBox="0 0 24 24"><path d="M2 5h20v14H2z"/><path d="M2 5l10 8 10-8" stroke="#fff" stroke-width="2" fill="none"/></svg>
          MarlowYoga@mailbox.example
        </li>
      </ul>
    </div>
  </div>
</body>
</html>
```